K&R Security Services PTY. LTD.

Ive just had my logo made and I'm looking for some simple but strong designs for my business cards the company is a security company.

Please use dark colors.

Regards,

Owen Deloit

Reason: Need more time for discussion with other directors

Industry/Entity Type

Security

Font styles to use
Sans Serif
Decorative

```html
<!DOCTYPE html>
<html lang="en">
<head>
<meta charset="utf-8">
<title>K&amp;R Security Services – Business Cards</title>
<link rel="stylesheet" href="https://fonts.googleapis.com/css2?family=Special+Elite&display=swap">
<style>
  :root {
    --page: #ffffff;
    --card-front: #fafafa;
    --card-back: #000000;
    --ink-light: #f2f2f2;
    --ink-mark: #4a4a4a;
    --rule: #8a8a8a;
    --shadow: rgba(0, 0, 0, 0.45);
  }
  html, body {
    margin: 0;
    width: 1200px;
    height: 900px;
    overflow: hidden;
    background: var(--page);
  }
  .canvas {
    position: relative;
    width: 1200px;
    height: 900px;
    font-family: "Special Elite", "Courier New", monospace;
  }
  .card {
    position: absolute;
    width: 393px;
    height: 222px;
    box-shadow: 0 6px 8px -2px var(--shadow);
  }
  .card--front {
    left: 195px;
    top: 339px;
    background: var(--card-front);
    display: flex;
    align-items: center;
    justify-content: center;
  }
  .brand-name {
    color: var(--ink-mark);
    font-size: 30px;
    letter-spacing: 1px;
    text-align: center;
    line-height: 1.15;
  }
  .card--back {
    left: 623px;
    top: 339px;
    background: var(--card-back);
    color: var(--ink-light);
    font-size: 14.5px;
    line-height: 20px;
  }
  .contact-grid {
    position: absolute;
    left: 17px;
    top: 22px;
    display: flex;
  }
  .contact-col {
    padding: 0 13px;
    border-left: 1px solid var(--rule);
  }
  .contact-col:first-child {
    padding-left: 0;
    border-left: none;
  }
  .contact-col p { margin: 0; }
  .email-line {
    position: absolute;
    left: 17px;
    bottom: 24px;
    margin: 0;
    white-space: nowrap;
  }
</style>
</head>
<body>
<main class="canvas">
  <section class="card card--front" aria-label="Card front">
    <div class="brand-name">K&amp;R<br>Security</div>
  </section>

  <section class="card card--back" aria-label="Card back">
    <div class="contact-grid">
      <div class="contact-col mobile">
        <p>0400</p><p>5551</p><p>28m</p>
      </div>
      <div class="contact-col phone">
        <p>(03)9</p><p>5550</p><p>418p</p>
      </div>
      <div class="contact-col address">
        <p>P.O. Box 7</p><p>Ashvale</p><p>Victoria 3199</p>
      </div>
    </div>
    <p class="email-line">e: owen@krsec.net.au / K.R@krsec.net.au</p>
  </section>
</main>
</body>
</html>
```